Business Card Design Project

A polished, very professional looking business card. I think we want to keep it all grey. I've attached our old logo, and current mockup in which case we really like the font.

Target Market(s)

Target Market are Bride and Grooms and Wedding Coordinators. We are wedding photographers

Industry/Entity Type

Business

Font styles to use
Serif
Sans Serif

Requirements
Must have
• An elegant, yet simple and sophisticated appearance.

Phone number, Email, Website and Social Media link.
Nice to have
• An element that can be spot glossed when printed. Not necessary though.
Should not have
• Bright colors, images or intensive graphics.

```html
<!DOCTYPE html>
<html lang="en">
<head>
<meta charset="utf-8">
<title>Calder Vane Photographers – Business Card</title>
<link rel="stylesheet" href="https://fonts.googleapis.com/css2?family=Marcellus+SC&family=Montserrat:wght@400;600;700&family=Questrial&display=swap">
<style>
  :root {
    --backdrop: #6a6a6c;
    --card-dark: #3a3a3c;
    --card-light: #ffffff;
    --accent-grey: #a8a8ab;
    --line-grey: #8a8a8d;
    --ink-light: #ffffff;
    --ink-dark: #3c3c3e;
    --ink-soft: #8d8d90;
  }
  html, body {
    margin: 0;
    width: 1200px;
    height: 1000px;
    overflow: hidden;
    background: var(--backdrop);
  }
  .canvas {
    position: relative;
    width: 1200px;
    height: 1000px;
  }
  .card {
    position: absolute;
    top: 341px;
    width: 544px;
    height: 318px;
    box-shadow: 0 4px 14px rgba(0,0,0,0.35);
  }
  .card--front { left: 46px; background: var(--card-dark); }
  .card--back  { left: 628px; background: var(--card-light); }
  .card svg { display: block; }

  .contact-name { font-family: 'Montserrat', sans-serif; font-weight: 700; font-size: 23px; fill: var(--ink-light); }
  .contact-role { font-family: 'Questrial', sans-serif; font-size: 13px; fill: var(--ink-light); }
  .contact-line { font-family: 'Questrial', sans-serif; font-size: 13.5px; fill: var(--ink-light); }

  .brand {
    position: absolute;
    inset: 0;
    display: flex;
    flex-direction: column;
    align-items: center;
  }
  .brand-square {
    margin-top: 58px;
    width: 86px;
    height: 86px;
    background: var(--ink-dark);
  }
  .brand-rule {
    margin-top: 26px;
    width: 36px;
    height: 2px;
    border-radius: 1px;
    background: #c9c9cb;
  }
  .brand-name {
    margin-top: 20px;
    font-family: 'Marcellus SC', serif;
    font-size: 34px;
    letter-spacing: 3px;
    color: var(--ink-dark);
    line-height: 1;
  }
  .brand-tag {
    margin-top: 12px;
    font-family: 'Montserrat', sans-serif;
    font-weight: 600;
    font-size: 11px;
    letter-spacing: 5px;
    color: var(--ink-soft);
  }
</style>
</head>
<body>
<main class="canvas">

  <section class="card card--front" aria-label="Card front with contact details">
    <svg width="544" height="318" viewBox="0 0 544 318">
      <polygon class="corner-top" points="0,0 96,0 0,58" fill="var(--accent-grey)"/>
      <polygon class="corner-bottom" points="430,318 544,318 544,252" fill="var(--accent-grey)"/>
      <line x1="340" y1="0" x2="0" y2="262" stroke="var(--line-grey)" stroke-width="1.5"/>
      <line x1="0" y1="166" x2="106" y2="318" stroke="var(--line-grey)" stroke-width="1.5"/>

      <g class="film-strip" fill="var(--ink-light)">
        <rect x="398" y="300" width="14" height="14" transform="rotate(-30 405 307)"/>
        <rect x="427" y="283" width="14" height="14" transform="rotate(-30 434 290)"/>
        <rect x="456" y="266" width="14" height="14" transform="rotate(-30 463 273)"/>
        <rect x="485" y="249" width="14" height="14" transform="rotate(-30 492 256)"/>
        <rect x="514" y="232" width="14" height="14" transform="rotate(-30 521 239)"/>
      </g>

      <g class="contact" transform="translate(42 172) rotate(-30)">
        <text class="contact-name" x="0" y="0">Owen Marsh</text>
        <text class="contact-role" x="18" y="22">Camera Operator</text>

        <g class="icon-phone" transform="translate(22 54)" fill="var(--ink-light)">
          <path d="M0 -9 h3 l1 3 l-2 1.5 q1 2.5 3 3.5 l1.5 -2 l3 1 v3 q-7 0 -9.5 -10z" transform="scale(0.8)"/>
        </g>
        <text class="contact-line" x="36" y="58">555.014.2280</text>

        <g class="icon-globe" transform="translate(27 73)" fill="none" stroke="var(--ink-light)" stroke-width="1.2">
          <circle r="5"/>
          <ellipse rx="2.2" ry="5"/>
          <line x1="-5" y1="0" x2="5" y2="0"/>
        </g>
        <text class="contact-line" x="36" y="78">www.marshlenswork.com</text>

        <text class="contact-line" x="36" y="100">1480 Alder Ave. xxx city</text>
        <text class="contact-line" x="36" y="120">Fairview, CA 90000</text>
      </g>
    </svg>
  </section>

  <section class="card card--back" aria-label="Card back with studio name">
    <div class="brand">
      <div class="brand-square"></div>
      <div class="brand-rule"></div>
      <div class="brand-name">Calder Vane</div>
      <div class="brand-tag">PHOTOGRAPHERS</div>
    </div>
  </section>

</main>
</body>
</html>
```